Fresh Nest Builder Guide needs a new Landing Page

I like to get a landing page or website with 2-3 pages to help target home buyers who are looking to buy homes from builders such as PV Dwellings, Moritz, G.T. Falwick, etc. The landing page/website to be non-cluttered and be able to explain to home buyers that there are many benefits to include me as their buyer's agent when they buy a brand new home from any builders.
I may want to incorporate a short explanation video (animated) on the landing page and then for the viewer to click on a button that will take them to another page where they can search for new homes from different builders.
Target Market(s)
Home buyers looking to buy brand new home from builders such as PV Dwellings, Moritz, G.T. Falwick, etc.
Industry/Entity Type
Real Estate
Number of Pages Required
2 page
Requirements
Must have
- The landing page may have the explanation video at the bottom of the landing page (scrolled down) or there may be a CALL TO ACTION button that takes the viewer to the 2nd page to watch the explanation video. Once they watched the explanation video and are still interested, they can click on another CALL TO ACTION button that will take them to another website that they will be able to search for all the available new homes and register their contact information.
Should not have
- No clutters and no dark colors.

```html
<!DOCTYPE html>
<html lang="en">
<head>
<meta charset="UTF-8">
<title>Home Community</title>
<link rel="stylesheet" href="https://fonts.googleapis.com/css2?family=Roboto:wght@300;400;500&display=swap">
<style>
  :root {
    --brand-pink: #d56aa8;
    --page-bg: #ebebeb;
    --ink: #343840;
    --video-bg: #353940;
    --header-text: #ffffff;
  }
  * { box-sizing: border-box; margin: 0; padding: 0; }
  html, body {
    width: 1200px;
    height: 600px;
    overflow: hidden;
  }
  body {
    position: relative;
    background: var(--page-bg);
    font-family: "Roboto", Arial, sans-serif;
    color: var(--ink);
  }
  .site-header {
    position: absolute;
    top: 0; left: 0;
    width: 1200px;
    height: 100px;
    background: var(--brand-pink);
  }
  .site-name {
    position: absolute;
    left: 140px;
    top: 33px;
    font-size: 24px;
    font-weight: 500;
    color: var(--header-text);
    line-height: 30px;
  }
  .main-nav {
    position: absolute;
    right: 118px;
    top: 39px;
    display: flex;
    gap: 9px;
  }
  .main-nav a {
    font-size: 17px;
    font-weight: 500;
    color: var(--header-text);
    text-decoration: none;
    line-height: 22px;
  }
  .hero-copy {
    position: absolute;
    left: 133px;
    top: 233px;
    width: 420px;
  }
  .hero-heading {
    font-size: 38px;
    font-weight: 500;
    line-height: 48px;
    color: var(--ink);
  }
  .hero-text {
    margin-top: 17px;
    font-size: 17px;
    font-weight: 300;
    line-height: 22px;
    color: var(--ink);
  }
  .cta-button {
    position: absolute;
    left: 130px;
    top: 399px;
    width: 220px;
    height: 58px;
    border: 2px solid var(--brand-pink);
    border-radius: 7px;
    display: flex;
    align-items: center;
    justify-content: center;
    font-size: 24px;
    font-weight: 300;
    color: var(--brand-pink);
    text-decoration: none;
  }
  .explainer-video {
    position: absolute;
    left: 610px;
    top: 191px;
    width: 460px;
    height: 300px;
    background: var(--video-bg);
  }
  .explainer-video svg { display: block; }
</style>
</head>
<body>
  <header class="site-header">
    <div class="site-name">Home Community</div>
    <nav class="main-nav">
      <a href="#">About Us</a>
      <a href="#">Services</a>
      <a href="#">Community</a>
      <a href="#">Gallery</a>
      <a href="#">Contact Us</a>
    </nav>
  </header>

  <section class="hero-copy">
    <h1 class="hero-heading">Heading Text</h1>
    <p class="hero-text">Lorem ipsum dolor sit amet, consectetur adipiscing elit, sed do eiusmod tempor incididunt ut labore et dolore magna aliqua.</p>
  </section>

  <a class="cta-button" href="#">Browse Now</a>

  <div class="explainer-video" role="img" aria-label="Explanation video player">
    <svg width="460" height="300" viewBox="0 0 460 300">
      <circle cx="230" cy="154" r="68" fill="none" stroke="var(--brand-pink)" stroke-width="3"/>
      <path d="M214 125 Q213 120 218 123 L256 150 Q260 154 256 158 L218 185 Q213 188 214 183 Z" fill="var(--brand-pink)"/>
    </svg>
  </div>
</body>
</html>
```